A need a professional website for An IT Company

We need a very professional but clean wordpress design for our website.
We are into IT solutions, we manage serrvers, unified communications and do computer repairs and maintenance. We want a wordpress design that will promote our offering and online presense greatly. Our design should be very clean and mordern for easy navigation.
Industry/Entity Type
Communications
Requirements
Must have
- A frontpage slider
contact form with Google map integration

```html
<!DOCTYPE html>
<html lang="en">
<head>
<meta charset="utf-8">
<title>Corvanta — IT Solutions</title>
<link rel="stylesheet" href="https://fonts.googleapis.com/css2?family=Open+Sans:wght@400;600&family=Arimo:wght@400;700&display=swap">
<style>
:root{
  --plum-dark:#3e1c33;
  --plum:#6a2f57;
  --plum-light:#9a5a8a;
  --maroon:#5c2636;
  --accent:#5c2a4a;
  --olive:#5e7a34;
  --sage:#8fa670;
  --ink:#333;
  --grey:#666;
  --line:#c9c2a4;
  --white:#fff;
}
*{box-sizing:border-box;margin:0;padding:0}
html,body{width:800px;height:1200px;overflow:hidden}
body{position:relative;background:var(--white);font-family:"Arimo",Arial,sans-serif;color:var(--ink)}
.abs{position:absolute}

.site-header{left:0;top:0;width:800px;height:122px;
  background:linear-gradient(115deg,var(--plum-dark) 0%,var(--plum) 45%,var(--plum-light) 70%,var(--plum) 100%)}
.logo-box{left:16px;top:9px;width:201px;height:70px;background:var(--white);border-radius:4px;box-shadow:0 1px 4px rgba(0,0,0,.4)}
.logo-name{left:18px;top:18px;font:600 27px "Open Sans",sans-serif;color:var(--plum);letter-spacing:1px;line-height:34px}
.search-field{left:542px;top:44px;width:184px;height:19px;background:#c7cdb6;border-radius:3px}
.search-btn{left:735px;top:43px;width:48px;height:20px;background:#111;color:#fff;font:400 10px "Open Sans",sans-serif;line-height:20px;text-align:center;border-radius:3px}

.main-nav{left:16px;top:89px;width:774px;height:33px;background:linear-gradient(#fff,#e3e3e3);border-radius:3px 3px 0 0;display:flex}
.main-nav span{font:400 11px "Open Sans",sans-serif;color:#222;line-height:33px;border-right:1px solid #ccc;text-align:center;white-space:nowrap}

.slider-frame{left:17px;top:121px;width:773px;height:259px;background:#1d1d1d;box-shadow:0 10px 12px -6px rgba(0,0,0,.35)}
.slide{left:26px;top:130px;width:757px;height:240px;background:#fff;border-radius:6px;overflow:hidden}
.slide-art{left:10px;top:6px;width:420px;height:228px;background:radial-gradient(ellipse at 45% 55%,#e4e8ee,#fafafa 70%)}
.slide-title{left:447px;top:88px;font:400 27px "Open Sans",sans-serif;color:var(--accent)}
.slide-sub{left:447px;top:130px;font:400 23px "Open Sans",sans-serif;color:var(--olive)}
.slide-corner{right:0;bottom:0}
.slide-arrow{top:234px;width:43px;height:41px;background:#3a3a3a}

.service h3{font:400 13px "Open Sans",sans-serif;color:#555;padding-bottom:4px;border-bottom:1px solid var(--line);white-space:nowrap}
.service .pic{margin-top:8px;height:122px;border:3px solid #fff;box-shadow:0 1px 5px rgba(0,0,0,.35)}
.service p{margin:14px 0 0 5px;font-size:9.8px;line-height:15px;color:var(--grey);white-space:nowrap}
.more{font-size:9px;color:var(--maroon)}
.service .more{display:block;margin:8px 0 0 8px}

.section-title{font:400 15px "Arimo",sans-serif;color:var(--ink)}
.section-title em{font-style:normal;color:var(--accent)}
.dots{height:0;border-top:1px dotted #888}
.welcome-copy{left:258px;top:709px;width:268px;font-size:10.4px;line-height:16.9px;color:var(--ink)}

.brand{top:934px;height:48px;border:1px solid #aaa;border-radius:4px;font:700 15px "Arimo",sans-serif;color:#555;display:flex;align-items:center;justify-content:center}
.brand.filled{background:#2b5ea8;color:#fff;border-color:#2b5ea8}

.areas{list-style:none;font-size:10.5px;color:var(--ink)}
.areas li{height:17px;padding-left:16px;position:relative;white-space:nowrap}
.areas li::before{content:"";position:absolute;left:0;top:3px;width:8px;height:8px;border-radius:50%;background:#555}

.side-panel{left:568px;width:210px;background:linear-gradient(#fafafa,#e6e6e6);border-radius:6px;box-shadow:0 1px 5px rgba(0,0,0,.35)}
.ribbon{left:552px;width:225px;height:25px;background:var(--maroon);color:#fff;font:400 12px "Arimo",sans-serif;line-height:25px;padding-left:26px}
.ribbon-fold{left:552px;width:16px;height:14px}
.field-label{left:560px;width:64px;text-align:right;font-size:10px;color:#444}
.field{left:634px;width:122px;height:17px;background:#fff;border:1px solid #c6c6c6;border-radius:3px}
.submit{left:705px;top:860px;width:53px;height:20px;background:var(--sage);border-radius:3px;font:700 10px "Arimo",sans-serif;line-height:20px;text-align:center;color:#222}
.map{left:573px;top:957px;width:203px;height:170px;background:linear-gradient(135deg,#e9df9e,#cfd6a8 55%,#b8c7b3)}

.site-footer{left:0;top:1140px;width:800px;height:60px;background:linear-gradient(115deg,var(--plum-dark),var(--plum) 50%,var(--plum-light) 75%,var(--plum))}
.foot-links{left:478px;top:1153px;font-size:10px;color:#fff;white-space:nowrap}
.copyright{left:561px;top:1178px;font-size:10px;color:#fff;white-space:nowrap}
.social{top:1166px;width:21px;height:21px;border-radius:3px}
</style>
</head>
<body>

<header class="abs site-header"></header>
<div class="abs logo-box">
  <span class="abs logo-name">CORVANTA</span>
</div>
<div class="abs search-field"></div>
<div class="abs search-btn">Search</div>

<nav class="abs main-nav">
  <span style="width:105px">Home</span>
  <span style="width:113px">About Us</span>
  <span style="width:113px">Services</span>
  <span style="width:164px">Areas of Specialisation</span>
  <span style="width:96px">Portfolio</span>
  <span style="width:110px;border:0">Contact Us</span>
</nav>

<div class="abs slider-frame"></div>
<div class="abs slide">
  <div class="abs slide-art" role="img" aria-label="Illustration of laptops linked to a central server and folders"></div>
  <div class="abs slide-title">Technologies</div>
  <div class="abs slide-sub">of the 21 st century!</div>
  <svg class="abs slide-corner" width="115" height="95" viewBox="0 0 115 95">
    <polygon points="0,95 115,0 115,95" fill="#8fa670"/>
    <text x="78" y="70" transform="rotate(-50 78 70)" font-family="Open Sans,sans-serif" font-size="12" fill="#222" text-anchor="middle">CLICK HERE</text>
  </svg>
</div>
<div class="abs slide-arrow" style="left:17px">
  <svg width="43" height="41"><polyline points="25,13 17,20.5 25,28" fill="none" stroke="#fff" stroke-width="3"/></svg>
</div>
<div class="abs slide-arrow" style="left:748px">
  <svg width="43" height="41"><polyline points="18,13 26,20.5 18,28" fill="none" stroke="#fff" stroke-width="3"/></svg>
</div>

<section class="abs service" style="left:37px;top:411px;width:194px">
  <h3>Computer Consultancy</h3>
  <div class="pic" role="img" aria-label="Photo of a consultant presenting a chart to colleagues" style="background:linear-gradient(#f2f2f2,#9aa3ad)"></div>
  <p>Nunc varius facilisis eros. Sed erat. In in velit<br>quis arcu ornare laoreet. luctus massa.</p>
  <span class="more">Click Here</span>
</section>
<section class="abs service" style="left:290px;top:411px;width:197px">
  <h3>Computer Maintenance &amp; Repairs</h3>
  <div class="pic" role="img" aria-label="Photo of a technician repairing a computer tower" style="background:linear-gradient(#f6f6f6,#c6ccd4)"></div>
  <p>Nunc varius facilisis eros. Sed erat. In in velit<br>quis arcu ornare laoreet. luctus massa.</p>
  <span class="more">Click Here</span>
</section>
<section class="abs service" style="left:555px;top:411px;width:197px">
  <h3>Computer Training</h3>
  <div class="pic" role="img" aria-label="Photo of trainees seated at computers in a classroom" style="background:linear-gradient(#eef3f8,#a9b8c8)"></div>
  <p>Nunc varius facilisis eros. Sed erat. In in velit<br>quis arcu ornare laoreet. luctus massa.</p>
  <span class="more">Click Here</span>
</section>

<h2 class="abs section-title" style="left:33px;top:668px">WELCOME TO <em>CORVANTA</em></h2>
<div class="abs dots" style="left:33px;top:696px;width:223px"></div>
<div class="abs" role="img" aria-label="Illustration of servers networked around a globe" style="left:38px;top:710px;width:210px;height:105px;background:radial-gradient(ellipse at 50% 50%,#d0d4d6,#fafafa 70%)"></div>
<p class="abs welcome-copy">In today’s high competitive world businesses of us sizes have started viewing computers as an expense. Every company that we survive today must see computer systems and IT support not just as integral part their business but also as a strategic part of business growth and management, helping to drastically reduce total operational costs and create new viable business opportunities for their business</p>
<span class="abs more" style="left:473px;top:849px">Click Here</span>
<div class="abs dots" style="left:32px;top:873px;width:491px"></div>

<h2 class="abs section-title" style="left:35px;top:898px;font-size:14px">OUR <em>BRANDS</em></h2>
<div class="abs brand filled" style="left:41px;width:75px">Pellan</div>
<div class="abs brand" style="left:131px;width:89px">Trevo</div>
<div class="abs brand" style="left:228px;width:89px">Lumora</div>
<div class="abs brand" style="left:325px;width:89px">Kestrel</div>
<div class="abs brand" style="left:422px;width:89px">Ondara</div>
<div class="abs dots" style="left:32px;top:1006px;width:491px"></div>

<h2 class="abs section-title" style="left:36px;top:1027px;font-size:14px">AREAS OF <em>SPECIALISATION</em></h2>
<ul class="abs areas" style="left:45px;top:1057px">
  <li>IT Outsourcing</li>
  <li>IT Consulting</li>
  <li>Server Virtualisation&nbsp; and Integration</li>
  <li>Network Security</li>
</ul>
<ul class="abs areas" style="left:345px;top:1058px">
  <li>Unified Communications</li>
  <li>Software Development</li>
  <li>Web Portal Development</li>
  <li>Server Consolidation</li>
</ul>
<span class="abs more" style="left:496px;top:1120px">Click Here</span>

<aside>
  <div class="abs side-panel" style="top:683px;height:212px"></div>
  <svg class="abs ribbon-fold" style="top:686px" width="16" height="11"><polygon points="16,0 16,11 0,11" fill="#3a1521"/></svg>
  <div class="abs ribbon" style="top:697px">Quick Contact Form</div>
  <span class="abs field-label" style="top:741px">Name&nbsp; :</span>
  <span class="abs field-label" style="top:767px">Email :</span>
  <span class="abs field-label" style="top:793px">Phone :</span>
  <span class="abs field-label" style="top:820px">Message&nbsp; :</span>
  <div class="abs field" style="top:739px"></div>
  <div class="abs field" style="top:763px"></div>
  <div class="abs field" style="top:788px"></div>
  <div class="abs field" style="top:813px;height:33px"></div>
  <div class="abs submit">SUBMIT</div>

  <div class="abs side-panel" style="top:915px;height:213px"></div>
  <svg class="abs ribbon-fold" style="top:918px" width="16" height="11"><polygon points="16,0 16,11 0,11" fill="#3a1521"/></svg>
  <div class="abs ribbon" style="top:929px">Find to Us</div>
  <div class="abs map" role="img" aria-label="Street map showing the office location with an address pop-up"></div>
</aside>

<footer class="abs site-footer"></footer>
<div class="abs foot-links">Privacy Policy &nbsp;&nbsp;&nbsp; | &nbsp;&nbsp;&nbsp; Terms &amp; Conditions &nbsp;&nbsp;&nbsp; | &nbsp;&nbsp;&nbsp; Contact Us</div>
<div class="abs copyright">© 2012 Corvanta, All Rights Reserved</div>
<div class="abs social" style="left:40px;background:#3b5a9a" role="img" aria-label="Social network link"></div>
<div class="abs social" style="left:65px;background:#3fa7d9" role="img" aria-label="Social network link"></div>
<div class="abs social" style="left:90px;background:#1f6fa8" role="img" aria-label="Social network link"></div>
<div class="abs social" style="left:115px;background:#e8842a" role="img" aria-label="News feed link"></div>

</body>
</html>
```